Atelier Marrow Architecture business card

We need to update our business card. We do high end custom residential, hospitality, and wellness architecture. We focus on creating unique spaces and design around the five senses, believing that architecture's true impact is not on our surroundings, but within us. We would like to see designs are instill a sense of calm awe. They should be crisp, fresh, clean, authentic, & contemporary without being sterile, overworked, or harsh. White space is important. Alternative materials are an option if natural. We have created our own logo and would like designs to incorporate it. However, we are willing to see alternatives if the logo becomes a stumbling block and you have an alternate you suggest. Card must have the following information:
Atelier Marrow Architecture, Inc.
728 Holloway Ct. NE Atlanta, GA 30318
Marcus T. Whitcombe, AIA, NCARB, LEED AP BD+C
ateliermarrow.example

Target Market(s)

Higher net worth individuals with an appreciation for design, nature, sustainability,

Industry/Entity Type

Architect

Contact Information for Business Card

See above. The title of Owner or Architect is helpful but not necessary. Minimalism should trump additional information.

Font styles to use
Serif
Sans Serif

Requirements
Must have
• It should look professional. It must use logo
Should not have
• caligraphy, animals, anything that is cute,

```html
<!DOCTYPE html>
<html lang="en">
<head>
<meta charset="utf-8">
<title>Atelier Marrow Architecture — Business Card</title>
<link rel="stylesheet" href="https://fonts.googleapis.com/css2?family=Marcellus&family=Quicksand:wght@500;700&display=swap">
<style>
  :root {
    --backdrop: #8c7a6b;
    --card-dark: #2a2a2a;
    --card-light: #ffffff;
    --accent: #ec7a1f;
    --wordmark: #3a3a3a;
    --text-light: #ffffff;
  }
  * { box-sizing: border-box; margin: 0; padding: 0; }
  html, body {
    width: 1200px; height: 801px; overflow: hidden;
    background: var(--backdrop);
  }
  .stage { position: relative; width: 1200px; height: 801px; }
  .card {
    position: absolute; top: 273px;
    width: 480px; height: 266px;
    background: var(--card-dark);
    overflow: hidden;
  }
  .card--front { left: 110px; }
  .card--back { left: 635px; }

  .wordmark {
    font-family: "Marcellus", Georgia, serif;
    font-weight: 400;
    color: var(--wordmark);
    text-transform: uppercase;
    letter-spacing: 0.22em;
    white-space: nowrap;
    text-align: center;
  }

  /* front */
  .front-band {
    position: absolute; left: 0; right: 0;
    top: 86px; height: 94px;
    background: var(--card-light);
    border-top: 2px solid var(--accent);
    border-bottom: 2px solid var(--accent);
    display: flex; align-items: center; justify-content: center;
  }
  .front-band .wordmark { font-size: 19px; }

  /* back */
  .back-header {
    position: absolute; left: 0; right: 0; top: 0;
    height: 121px;
    background: var(--card-light);
    border-bottom: 2px solid var(--accent);
    display: flex; align-items: center; justify-content: center;
    padding-bottom: 6px;
  }
  .back-header .wordmark { font-size: 18px; }

  .holder {
    position: absolute; left: 28px; top: 168px;
    font-family: "Quicksand", Arial, sans-serif;
  }
  .holder__name {
    color: var(--text-light);
    font-weight: 700; font-size: 19px; letter-spacing: -0.01em;
    line-height: 1.1;
  }
  .holder__credentials {
    color: var(--accent);
    font-weight: 500; font-size: 13px; letter-spacing: 0.04em;
    margin-top: 2px;
  }

  .contact {
    position: absolute; left: 255px; top: 161px;
    list-style: none;
    font-family: "Quicksand", Arial, sans-serif;
    font-weight: 500; font-size: 12px; line-height: 1.3;
    color: var(--text-light);
  }
  .contact__item { display: flex; align-items: flex-start; }
  .contact__item + .contact__item { margin-top: 11px; }
  .contact__icon {
    flex: 0 0 24px; width: 24px; height: 24px;
    border-radius: 3px; background: var(--accent);
    display: flex; align-items: center; justify-content: center;
    margin-right: 12px;
  }
  .contact__text { padding-top: 4px; }
</style>
</head>
<body>
<main class="stage">

  <section class="card card--front" aria-label="Card front">
    <div class="front-band">
      <p class="wordmark">Atelier Marrow Architecture</p>
    </div>
  </section>

  <section class="card card--back" aria-label="Card back">
    <header class="back-header">
      <p class="wordmark">Atelier Marrow Architecture</p>
    </header>

    <div class="holder">
      <p class="holder__name">Marcus T. Whitcombe</p>
      <p class="holder__credentials">AIA, NCARB, LEED AP BD+C</p>
    </div>

    <ul class="contact">
      <li class="contact__item">
        <span class="contact__icon">
          <svg width="14" height="14" viewBox="0 0 14 14" fill="none" stroke="#fff" stroke-width="1.1" aria-hidden="true">
            <circle cx="7" cy="7" r="5.8"/>
            <ellipse cx="7" cy="7" rx="2.5" ry="5.8"/>
            <line x1="1.2" y1="7" x2="12.8" y2="7"/>
            <line x1="2" y1="4" x2="12" y2="4"/>
            <line x1="2" y1="10" x2="12" y2="10"/>
          </svg>
        </span>
        <span class="contact__text">ateliermarrow.example</span>
      </li>
      <li class="contact__item">
        <span class="contact__icon">
          <svg width="12" height="15" viewBox="0 0 12 15" aria-hidden="true">
            <path d="M6 0.5C3 0.5 0.8 2.7 0.8 5.6 0.8 9.3 6 14.5 6 14.5S11.2 9.3 11.2 5.6C11.2 2.7 9 0.5 6 0.5Z" fill="#fff"/>
            <circle cx="6" cy="5.6" r="2" fill="#ec7a1f"/>
          </svg>
        </span>
        <span class="contact__text">728 Holloway Ct. NE Atlanta,<br>GA 30318</span>
      </li>
    </ul>
  </section>

</main>
</body>
</html>
```